Design an attractive wine label for Brell Fine Wines

we need a wine label design, we are an Australian wine exporting company'Brell Fine Wines'. We succeed several pallets in last few months and is going to launch our first container. So it’s time to start our own brands. we will have some wines display in China's shopping mall shelves, so we want to have a catchy label which can attract Chinese eyes immediately. other details you will see in the file i uploaded. The design should include a front and back label.

Target Market(s)

Brell Fine Wines are targeting middle class wine drinkers in 2nd-4th tier Chinese cities.

Colors

Designer to choose colors to be used in the design.

Requirements
Must have
• We’d like something that at first glance is Australian (element, style or color…) but subconsciously connects to the Chinese. Demeanor bearing in mind the demographics targeted across the ranges. We would expect the designs and naming to becoming more formalized as they rise to platinum.
Nice to have
• creative things come out
Should not have
• any dead related word or icon, no number '4' related word or icon, no skull related word or icon, kangaroo (see brand 'Copper vine')

```html
<!DOCTYPE html>
<html lang="en">
<head>
<meta charset="utf-8">
<title>Brell Fine Wines – Cabernet Sauvignon Front Label</title>
<link rel="stylesheet" href="https://fonts.googleapis.com/css2?family=Mrs+Saint+Delafield&family=Libre+Baskerville&display=swap">
<style>
  :root {
    --page: #ffffff;
    --label-cream: #ebebd9;
    --ink: #1f1a1a;
    --ink-soft: #3a3535;
    --gold: #c9ad74;
    --sun-yellow: #f2b62c;
    --sun-orange: #e9822a;
    --seal: #dcdcc8;
  }
  * { margin: 0; padding: 0; box-sizing: border-box; }
  html, body {
    width: 1200px;
    height: 1200px;
    overflow: hidden;
    background: var(--page);
  }
  .canvas {
    position: relative;
    width: 1200px;
    height: 1200px;
  }
  .front-label {
    position: absolute;
    left: 96px;
    top: 98px;
    width: 1008px;
    height: 1004px;
    background: var(--label-cream);
    border-radius: 6px;
    box-shadow: 0 2px 8px rgba(0, 0, 0, 0.08);
  }
  .brand-name {
    position: absolute;
    left: 0;
    right: 0;
    top: 190px;
    text-align: center;
    font-family: 'Libre Baskerville', serif;
    font-weight: 400;
    font-size: 70px;
    line-height: 1;
    letter-spacing: 6px;
    color: var(--ink);
  }
  .vineyard-scene {
    position: absolute;
    left: 252px;
    top: 337px;
    width: 495px;
    height: 288px;
  }
  .region {
    position: absolute;
    left: 0;
    right: 0;
    top: 690px;
    text-align: center;
    font-family: 'Mrs Saint Delafield', cursive;
    font-size: 58px;
    line-height: 1;
    color: var(--ink);
  }
  .variety {
    position: absolute;
    left: 0;
    right: 0;
    top: 758px;
    text-align: center;
    font-family: 'Libre Baskerville', serif;
    font-size: 17px;
    letter-spacing: 1.5px;
    color: var(--ink-soft);
  }
  .variety .variety-first { color: var(--gold); }
  .vintage {
    position: absolute;
    left: 0;
    right: 0;
    top: 796px;
    text-align: center;
    font-family: 'Libre Baskerville', serif;
    font-size: 18px;
    letter-spacing: 2px;
    color: var(--ink);
  }
  .region-seal {
    position: absolute;
    left: 54px;
    top: 770px;
  }
</style>
</head>
<body>
<main class="canvas">
  <section class="front-label">
    <h1 class="brand-name">SUNRIDGE</h1>

    <svg class="vineyard-scene" viewBox="0 0 495 288" role="img" aria-label="Etched vineyard landscape with rows of vines, a farmhouse and a watercolour sun">
      <defs>
        <linearGradient id="vineyard-tone" x1="0" y1="0" x2="1" y2="0">
          <stop offset="0" stop-color="#a7a599" stop-opacity="0.55"/>
          <stop offset="0.55" stop-color="#8c8a80" stop-opacity="0.7"/>
          <stop offset="0.75" stop-color="#f2b62c"/>
          <stop offset="1" stop-color="#e9822a"/>
        </linearGradient>
      </defs>
      <rect x="0" y="0" width="495" height="288" rx="10" fill="url(#vineyard-tone)"/>
    </svg>

    <p class="region">Australia</p>
    <p class="variety"><span class="variety-first">CABERNET</span> SAUVIGNON</p>
    <p class="vintage">2007</p>

    <svg class="region-seal" width="198" height="198" viewBox="0 0 198 198" aria-hidden="true">
      <circle cx="99" cy="99" r="96" fill="none" stroke="var(--seal)" stroke-width="3"/>
      <circle cx="99" cy="99" r="60" fill="none" stroke="var(--seal)" stroke-width="2"/>
    </svg>
  </section>
</main>
</body>
</html>
```